Chart Your Own Harbor Promotional Flyer

I Need a one page, one-sided 8.5 x 11 editable promotional flyer that POPS!, designed in photoshop

[TITLE]Chart Your Own Harbor: 3 BRIGHT Steps to Lift Your Practice Today!

[CONTENT for the Flyer:]

At this content-rich event you will learn how to:
• Get out of feast and famine mode and into six, multi-six and/or seven figure-income mode
• Leapfrog your competition and become the obvious choice in your market
• Have your business aligned with who you are and what you want
• Enjoy your business far more than you imagined possible.
• Have more fun and time to yourself
• Live free and unbound!

Accolades
“Delphine helped us increase our six figure income by 41%...I feel reborn!” Marlene & Otis Pruitt, Vienna, VA

“…Delphine is a joy to listen to - compelling, smart, provocative…” – Dwight Fennimore, Charlotte, North Carolina

“Delphine helped me increase my business by 66%...without me spending more time, money, or making cold calls! …I am in the zone!” Tess Calloway, Baltimore, MD
“Delphine is an energetic and dynamic speaker…content-rich…holds your attention to the very end!” Hal Brisbee, Frmr Pres., Kemper & Vail, MD, MD, D.C., PA, DE, NJ
“Delphine is the real estate whisperer!” Lou Tremaine, Washington D.C.

“Delphine was prepared, funny, informative and made a connection with each of our agents…Fabulous!…even my admins were PUMPED!!! – Paul Devereux, New York

About Delphine:
Delphine is a highly regarded business development speaker & coach who knows how to pump up an audience and have them making more money, in less time, AND having more fun doing it! What’s not to love?! Consistently rated as an exceptional speaker and conference favorite! Among her work: Magnet Method: How to Draw Your Dream Buyers Time After Time!, Client Pipelines Without Fuss, The Costliest Outreach Blunders Real Estate Agents Commit and How to Sidestep Them, Hard Seasons Forge Hard Sellers, Fuel for the Spirit for Real Estate Agents.

[Also need a section for:]
Date: December 9, 2015, Time: 9:00 Am - 12:00 Noon, Place: Silver Maple Conference, Ashford Hollow, PA

Target Market(s)

Real Estate Agents

Industry/Entity Type

Real Estate Agent

Font styles to use
Sans Serif

Colors
0655a3
f37122

Requirements
Must have
• the top tier prop mentor logo
Nice to have
• chart your own harbor logo; lots of POP! :-) ; open to other colors, accent colors.

```html
<!DOCTYPE html>
<html lang="en">
<head>
<meta charset="utf-8">
<title>Chart Your Own Harbor – Event Flyer</title>
<link href="https://fonts.googleapis.com/css2?family=Source+Sans+3:wght@400;600;700&display=swap" rel="stylesheet">
<style>
  :root {
    --navy: #0b1150;
    --orange: #ec7d2a;
    --paper: #f2f2f4;
    --backdrop: #8aa3a2;
    --ink: #14183f;
    --white: #ffffff;
  }
  * { margin: 0; padding: 0; box-sizing: border-box; }
  html, body {
    width: 1200px; height: 960px; overflow: hidden;
    background: var(--backdrop);
    font-family: "Source Sans 3", sans-serif;
  }
  .flyer {
    position: absolute; left: 272px; top: 16px;
    width: 656px; height: 928px;
    background: var(--paper);
    overflow: hidden;
    color: var(--ink);
  }
  .flyer__header {
    position: absolute; left: 0; top: 0; width: 100%; height: 50px;
    background: var(--navy);
    color: var(--white);
    display: flex; align-items: center; justify-content: center;
    font-size: 19px; font-weight: 600; letter-spacing: -0.2px;
  }
  .intro {
    position: absolute; left: 22px; top: 68px; width: 600px;
    font-size: 12.5px; line-height: 16.8px; letter-spacing: -0.2px;
  }
  .intro ul { list-style: none; }
  .intro li::before { content: "• "; }
  .section-title {
    color: var(--navy); font-weight: 700; font-size: 22px; line-height: 26px;
  }
  .accolades { position: absolute; left: 20px; top: 200px; width: 602px; }
  .accolades .section-title { margin-left: 2px; margin-bottom: 10px; }
  .quote {
    font-size: 12.5px; line-height: 16.8px; letter-spacing: -0.2px;
  }
  .quote--gap { margin-bottom: 16.8px; }
  .portrait {
    position: absolute; left: 21px; top: 490px; width: 164px; height: 199px;
    border: 2px solid var(--orange);
    background: linear-gradient(180deg, #e6e3df 0%, #b58d62 45%, #2b2622 100%);
  }
  .about { position: absolute; left: 203px; top: 505px; width: 420px; }
  .about .section-title { margin-bottom: 6px; }
  .about p {
    color: var(--navy); font-size: 12.8px; line-height: 16.8px; letter-spacing: -0.25px;
  }
  .waves { position: absolute; left: 0; top: 0; width: 656px; height: 928px; }
  .event {
    position: absolute; left: 380px; top: 745px; width: 270px;
    text-align: center; color: var(--navy);
  }
  .event__date { font-size: 24px; font-weight: 600; line-height: 30px; }
  .event__line { font-size: 13.5px; line-height: 20px; }
  .brand {
    position: absolute; left: 24px; top: 852px;
    display: flex; align-items: center; gap: 8px;
    color: var(--white); font-size: 19px; font-weight: 600;
  }
  .brand__dot {
    width: 12px; height: 12px; border-radius: 50%; background: var(--orange);
  }
</style>
</head>
<body>
<main class="flyer">
  <header class="flyer__header">Chart Your Own Harbor: 3 BRIGHT Steps to Lift Your Practice Today!</header>

  <section class="intro">
    <p>At this content-rich event you will learn how to:</p>
    <ul>
      <li>Get out of feast and famine mode and into six, multi-six and/or seven figure-income mode</li>
      <li>Leapfrog your competition and become the obvious choice in your market</li>
      <li>Have your business aligned with who you are and what you want</li>
      <li>Enjoy your business far more than you imagined possible.</li>
      <li>Have more fun and time to yourself</li>
      <li>Live free and unbound!</li>
    </ul>
  </section>

  <section class="accolades">
    <h2 class="section-title">Accolades</h2>
    <p class="quote quote--gap">“Delphine helped us increase our six figure income by 41%...I feel reborn!” Marlene &amp; Otis Pruitt, Vienna, VA</p>
    <p class="quote quote--gap">“…Delphine is a joy to listen to - compelling, smart, provocative…” – Dwight Fennimore, Charlotte, North Carolina</p>
    <p class="quote">“Delphine helped me increase my business by 66%...without me spending more time, money, or making cold calls! …I am in the zone!” Tess Calloway, Baltimore, MD</p>
    <p class="quote quote--gap">“Delphine is an energetic and dynamic speaker…content-rich…holds your attention to the very end!” Hal Brisbee, Frmr</p>
    <p class="quote">Pres., Kemper &amp; Vail, MD, MD, D.C., PA, DE, NJ</p>
    <p class="quote quote--gap">“Delphine is the real estate whisperer!” Lou Tremaine, Washington D.C.</p>
    <p class="quote">“Delphine was prepared, funny, informative and made a connection with each of our agents…Fabulous!…even my admins were PUMPED!!! – Paul Devereux, New York</p>
  </section>

  <div class="portrait" role="img" aria-label="Portrait photograph of speaker Delphine in a dark blazer"></div>

  <section class="about">
    <h2 class="section-title">About Delphine</h2>
    <p>Delphine is a highly regarded business development speaker &amp; coach who knows how to pump up an audience and have them making more money, in less time, AND having more fun doing it! What’s not to love?! Consistently rated as an exceptional speaker and conference favorite! Among her work: Magnet Method: How to Draw Your Dream Buyers Time After Time!, Client Pipelines Without Fuss, The Costliest Outreach Blunders Real Estate Agents Commit and How to Sidestep Them, Hard Seasons Forge Hard Sellers, Fuel for the Spirit for Real Estate Agents.</p>
  </section>

  <svg class="waves" viewBox="0 0 745 1055" preserveAspectRatio="none" aria-hidden="true">
    <ellipse cx="610" cy="890" rx="240" ry="142" fill="var(--orange)"/>
    <path d="M0,872 C90,818 230,830 330,915 C410,985 470,1040 540,1055 L0,1055 Z" fill="var(--navy)"/>
    <path d="M360,1000 C420,1030 470,1050 520,1055 L600,1055 C520,1045 440,1025 360,1000 Z" fill="var(--orange)"/>
    <path d="M165,818 C300,860 420,1005 560,1030 C640,1042 700,1035 745,1020 L745,1055 L560,1055 C440,1040 350,915 165,818 Z" fill="var(--navy)"/>
  </svg>

  <section class="event">
    <p class="event__date">December 9, 2015</p>
    <p class="event__line">9:00 Am - 12:00 Noon</p>
    <p class="event__line">at</p>
    <p class="event__line">Silver Maple Conference, Ashford Hollow, PA</p>
  </section>

  <div class="brand"><span class="brand__dot"></span>Chart Your Own Harbor</div>
</main>
</body>
</html>
```